KTR EVENTS & VISUALS WEBSITE DESIGN

Create a visually stimulating website for potential clients and vendors to effortlessly view our work. Sleek, classy vibe. Design should be clean, not too busy, yet visually enticing. Please refer to our old website and instagram for pictures and information. We still have our same philosophy & values, and our main goal is to create a fresh, new, inspiring look. (see below)

Website: www.ktreventsandvisuals.com
Instagram: ktreventsandvisuals

Target Market(s)

High end, Luxury wedding & event clients.

Industry/Entity Type

Event Planning

Number of Pages Required

5+ page

Font styles to use
Other font styles liked:
• Century Gothic

Colors

Designer to choose colors to be used in the design.

Requirements
Must have
• Lots of pictures/visual stimulation. Easy to access
• An abundance of photos capturing people, emotions, Beautiful event decor, & the venue itself.
Nice to have
• Trendy, up to date style
Should not have
• No detailed shots that show brand names

```html
<!DOCTYPE html>
<html lang="en">
<head>
<meta charset="utf-8">
<title>KTR Events &amp; Visuals — Website Design Presentation</title>
<link rel="stylesheet" href="https://fonts.googleapis.com/css2?family=Questrial&family=Source+Sans+3:wght@400;600;700&display=swap">
<style>
  :root{
    --board:#e6e8ec;
    --navy:#141a4a;
    --navy-deep:#0d1136;
    --blue:#4f7fcc;
    --blue-light:#6d96d6;
    --yellow:#fde04f;
    --white:#ffffff;
    --ink:#1d1d24;
    --muted:#6b6f80;
    --line:#c9d3e8;
  }
  *{box-sizing:border-box;margin:0;padding:0}
  html,body{width:800px;height:1200px;overflow:hidden;background:var(--board)}
  .board{position:relative;width:800px;height:1200px;background:var(--board);font-family:"Questrial",sans-serif;color:var(--ink)}
  .abs{position:absolute}

  /* site mockup */
  .site{position:absolute;left:54px;top:14px;width:299px;height:1170px;background:var(--white);box-shadow:6px 6px 10px rgba(0,0,0,.35);overflow:hidden}
  .site .abs{position:absolute}
  .hero{left:0;top:0;width:299px;height:168px;background:radial-gradient(circle at 70% 40%,#23307a,var(--navy) 55%,var(--navy-deep))}
  .brand{color:var(--white);font-size:10px;letter-spacing:.5px;display:flex;align-items:center;gap:3px}
  .brand .mark{width:8px;height:8px;border:1px solid var(--blue-light)}
  .nav{display:flex;gap:9px;font-size:3.4px;color:#c8cde8}
  .nav .on{color:var(--yellow)}
  .social{display:flex;gap:2px}
  .social i{display:block;width:5px;height:5px;border:0.6px solid #c8cde8;border-radius:50%}
  .hero-kicker{color:var(--white);font-size:9px;letter-spacing:.3px}
  .hero-kicker span{color:var(--yellow)}
  .hero-title{color:var(--white);font-size:10.5px;font-weight:700;letter-spacing:.3px;font-family:"Source Sans 3",sans-serif}
  .btn{font-size:3.4px;display:flex;align-items:center;justify-content:center;border:0.6px solid var(--blue-light);color:var(--blue)}
  .btn.outline-gold{border-color:var(--yellow);color:var(--white)}
  .btn.solid{background:var(--blue);color:var(--white);border-color:var(--blue)}
  .photo{display:block}
  .h-light{color:var(--blue-light);font-size:12px;line-height:1.2;letter-spacing:.3px}
  .small{font-size:3.2px;line-height:1.4;color:var(--muted)}
  .body{font-size:6.4px;line-height:1.3;color:var(--ink)}
  .card{width:62px;height:62px;border:0.6px solid var(--line);background:var(--white);display:flex;flex-direction:column;align-items:center;justify-content:flex-end;padding-bottom:14px;font-size:3.6px;color:#333}
  .card svg{margin-bottom:9px}
  .card.active{background:var(--blue);color:var(--white);justify-content:flex-start;padding:8px 5px 0;font-size:3px;text-align:center;line-height:1.4}
  .testimonials{left:0;top:426px;width:299px;height:158px;background:radial-gradient(circle at 50% 50%,#2a3a99,var(--navy) 60%,var(--navy-deep))}
  .section-title{width:299px;text-align:center;color:var(--blue-light);font-size:11.5px}
  .section-sub{width:299px;text-align:center;font-size:3.6px;letter-spacing:.4px;font-weight:700;font-family:"Source Sans 3",sans-serif}
  .quote{width:190px;left:55px;text-align:center;color:#dfe3f6;font-size:3.6px;line-height:2.1}
  .blog{left:22px;top:872px;width:268px;height:120px;background:#faf9fb}
  .post{width:130px;height:56px}
  .post .thumb{position:absolute;left:0;top:8px;width:44px;height:44px}
  .post .meta{position:absolute;left:51px;top:8px;width:80px}
  .post .date{font-size:2.6px;color:var(--muted)}
  .post .ttl{font-size:3.4px;font-weight:700;letter-spacing:.3px;line-height:1.5;margin:2px 0;font-family:"Source Sans 3",sans-serif}
  .field{border-bottom:0.6px solid var(--line);font-size:2.8px;color:var(--muted);height:8px}
  .footer-bar{left:0;top:1160px;width:299px;height:10px;background:var(--navy)}

  /* presentation notes */
  .notes{position:absolute;left:433px;top:0;font-family:"Source Sans 3",sans-serif;color:var(--ink)}
  .notes .t{position:absolute;white-space:nowrap}
  .n-head{font-size:11px}
  .n-head b{font-weight:700}
  .n-sub{font-size:11.5px;font-weight:700}
  .n-item{font-size:9px}
  .n-list{font-size:9px;line-height:11.6px}
  .n-big{font-size:19px;line-height:24px}
  .n-ps{font-size:13px}
</style>
</head>
<body>
<div class="board">

  <section class="site">
    <!-- hero -->
    <div class="abs hero"></div>
    <div class="abs brand" style="left:16px;top:14px"><span class="mark"></span>KTR</div>
    <nav class="abs nav" style="left:112px;top:22px"><span class="on">Home</span><span>About</span><span>Services</span><span>Venues</span><span>Gallery</span><span class="on">Events</span><span>Reviews</span><span>Contact</span></nav>
    <div class="abs social" style="left:274px;top:21px"><i></i><i></i></div>
    <div class="abs" style="left:132px;top:32px;width:136px;height:120px;background:var(--yellow)"></div>
    <div class="abs photo" role="img" aria-label="Portrait of the lead event planner leaning on the yellow wall" style="left:176px;top:46px;width:70px;height:106px;background:linear-gradient(180deg,#e7c55a,#b9a27a 45%,#8c8c94)"></div>
    <div class="abs" style="left:120px;top:24px;width:16px;height:18px;background:var(--blue)"></div>
    <div class="abs" style="left:262px;top:68px;width:14px;height:14px;background:var(--navy-deep)"></div>
    <div class="abs" style="left:244px;top:80px;width:44px;height:44px;background:var(--blue)"></div>
    <div class="abs hero-kicker" style="left:16px;top:85px">AN ENTIRELY <span>DIFFERENT</span></div>
    <div class="abs hero-title" style="left:16px;top:98px">EVENT PLANNING EXPERIENCE</div>
    <div class="abs btn outline-gold" style="left:18px;top:125px;width:43px;height:10px">About Marco Reyes</div>
    <div class="abs btn solid" style="left:64px;top:125px;width:45px;height:10px">Services</div>

    <!-- intro -->
    <div class="abs" style="left:18px;top:164px;width:72px;height:8px;background:var(--blue)"></div>
    <div class="abs" style="left:80px;top:226px;width:74px;height:58px;background:var(--yellow)"></div>
    <div class="abs photo" role="img" aria-label="Wedding couple in a grand ballroom decorated with white flowers" style="left:22px;top:172px;width:118px;height:103px;background:linear-gradient(160deg,#b98a62,#e9dcd2 40%,#7b5438 80%)"></div>
    <div class="abs h-light" style="left:163px;top:196px">GET YOUR EVENT<br>COVERED</div>
    <div class="abs small" style="left:163px;top:223px;width:115px;color:#333">The most beautiful things are not measured in money, they are memories and moments.</div>
    <div class="abs body" style="left:163px;top:246px">We take care of preparation,<br>you enjoy the celebration</div>

    <!-- services -->
    <div class="abs card" style="left:17px;top:310px"><svg width="22" height="26" viewBox="0 0 22 26" fill="none" stroke="#1d2a6b" stroke-width="1"><path d="M2 25V9Q11-4 20 9v16"/><path d="M5 25V11Q11 2 17 11v14"/><path d="M1 25h20"/></svg>Event Planning &amp; Design</div>
    <div class="abs card" style="left:83px;top:310px"><svg width="24" height="24" viewBox="0 0 24 24" fill="none" stroke="#1d2a6b" stroke-width="1"><rect x="4" y="2" width="15" height="20"/><path d="M7 7h9M7 11h9M7 15h9M2 5v17h3M19 22h3V5"/></svg>Partial Event Planning</div>
    <div class="abs card" style="left:149px;top:310px"><svg width="22" height="24" viewBox="0 0 22 24" fill="none" stroke="#1d2a6b" stroke-width="1"><path d="M1 2h20M3 2v10M19 2v10"/><path d="M11 8v4"/><rect x="9" y="12" width="4" height="6"/><path d="M11 18v5"/></svg>Event Production</div>
    <div class="abs card active" style="left:215px;top:310px">Day-Of Coordination<br><br>Let our team step in during the final weeks so every detail runs smoothly on your day.<br><br>This package includes a timeline, vendor follow up and on-site lead.</div>
    <div class="abs btn" style="left:125px;top:380px;width:46px;height:10px">Check Our Services</div>
    <div class="abs" style="left:240px;top:396px;width:36px;height:16px;background:var(--yellow)"></div>

    <!-- testimonials -->
    <div class="abs testimonials"></div>
    <div class="abs section-title" style="left:0;top:444px">What our clients said</div>
    <div class="abs section-sub" style="left:0;top:460px;color:var(--white)">REVIEWS</div>
    <div class="abs quote" style="top:471px">KTR Events could not have been more amazing. They took our ideas and visions and made them better and more perfect than we could have imagined. They were by our side every step of the way, and with only 6 months from engagement to wedding, we did not think it was possible to achieve everything they did for us. Our day was absolutely flawless. Thank you, KTR Events and Visuals.</div>
    <div class="abs" style="left:0;top:513px;width:299px;text-align:center;font-size:3.6px;color:var(--yellow);line-height:2">Nina<br><br>Wedding 10/24/2014<br>Services Used: Wedding Planning Reviewed On 10/27/2014</div>
    <svg class="abs" style="left:20px;top:498px" width="6" height="12" viewBox="0 0 6 12" fill="none" stroke="#6d7ab8" stroke-width=".8"><path d="M5 1L1 6l4 5"/></svg>
    <svg class="abs" style="left:273px;top:498px" width="6" height="12" viewBox="0 0 6 12" fill="none" stroke="#6d7ab8" stroke-width=".8"><path d="M1 1l4 5-4 5"/></svg>
    <div class="abs" style="left:16px;top:544px;width:40px;height:40px;background:var(--blue)"></div>
    <div class="abs" style="left:48px;top:565px;width:16px;height:16px;background:var(--yellow)"></div>

    <!-- gallery -->
    <div class="abs section-title" style="left:0;top:594px">Latest Events</div>
    <div class="abs section-sub" style="left:0;top:611px">GALLERY</div>
    <div class="abs photo" role="img" aria-label="Ballroom reception with tall floral centerpieces" style="left:20px;top:627px;width:85px;height:85px;background:linear-gradient(160deg,#7a4a7a,#d8b9a8 50%,#8a5a4a)"></div>
    <div class="abs photo" role="img" aria-label="Bride and groom under purple uplit floral arch" style="left:108px;top:627px;width:85px;height:85px;background:linear-gradient(160deg,#5a3a8a,#d6c3e0 50%,#6a4a7a)"></div>
    <div class="abs photo" role="img" aria-label="Art show event in New York with blue overlay" style="left:196px;top:627px;width:85px;height:85px;background:linear-gradient(160deg,#5b87d2,#4a78c8)"></div>
    <div class="abs" style="left:204px;top:690px;font-size:3.6px;color:var(--yellow);font-weight:700;font-family:'Source Sans 3',sans-serif">SHOWS</div>
    <div class="abs" style="left:204px;top:696px;font-size:7px;color:var(--white)">Art Show NYC</div>
    <div class="abs btn" style="left:128px;top:724px;width:43px;height:9px">More Galleries</div>

    <!-- budget -->
    <div class="abs" style="left:195px;top:755px;width:57px;height:55px;background:var(--yellow)"></div>
    <div class="abs" style="left:24px;top:772px;font-size:12px;line-height:14.5px;color:#4a5a8a">Plan your event budget:<br>there should be only good surprises</div>
    <div class="abs btn solid" style="left:224px;top:800px;width:43px;height:10px">Calculate</div>

    <!-- blog -->
    <div class="abs section-title" style="left:0;top:839px">Get Inspired &amp; Celebrate</div>
    <div class="abs section-sub" style="left:0;top:857px">OUR BLOG</div>
    <div class="abs blog">
      <div class="abs post" style="left:0;top:0">
        <div class="thumb" role="img" aria-label="Children's party performer with lanterns" style="background:linear-gradient(150deg,#d07a30,#6a2a14)"></div>
        <div class="meta"><div class="date">October 18, 2017</div><div class="ttl">BEST CHOICE FOR CHILDREN'S PARTY</div><div class="small">Fresh ideas for themed decor, games and treats that keep young guests happy all day.</div></div>
      </div>
      <div class="abs post" style="left:128px;top:0">
        <div class="thumb" role="img" aria-label="Guest celebrating at an elegant dinner" style="background:linear-gradient(150deg,#c9a88a,#4a3a30)"></div>
        <div class="meta"><div class="date">December 1, 2017</div><div class="ttl">MUST-HAVE TOOLS FOR BETTER EVENTS</div><div class="small">The planning tools our team relies on to keep every timeline and vendor on track.</div></div>
      </div>
      <div class="abs post" style="left:0;top:54px">
        <div class="thumb" role="img" aria-label="Carnival dancer in feathered costume" style="background:linear-gradient(150deg,#6a8acb,#b05a6a)"></div>
        <div class="meta"><div class="date">November 27, 2017</div><div class="ttl">STARTING AN EVENT PLANNING SERVICE</div><div class="small">What we learned while building a planning studio from the first client onward.</div></div>
      </div>
      <div class="abs post" style="left:128px;top:54px">
        <div class="thumb" role="img" aria-label="Friends toasting around a dinner table" style="background:linear-gradient(150deg,#d8b89a,#6a4a3a)"></div>
        <div class="meta"><div class="date">November 9, 2017</div><div class="ttl">HOW TO START AN EVENT PLANNING SERVICE</div><div class="small">A short guide to pricing, contracts and finding trusted vendors for your events.</div></div>
      </div>
    </div>

    <!-- contact -->
    <div class="abs photo" role="img" aria-label="Underwater pool party scene in bright blue water" style="left:22px;top:1006px;width:158px;height:104px;background:linear-gradient(170deg,#6a8ad8,#a9c4ee 50%,#3a6ac0)"></div>
    <div class="abs" style="left:24px;top:1007px;font-size:12px;white-space:nowrap;color:var(--blue)"><span style="color:var(--navy)">We know how to make so</span><span style="color:var(--yellow)">mething special</span></div>
    <div class="abs" style="left:196px;top:1034px;width:80px;text-align:center;font-size:7px;line-height:8.5px;color:var(--blue-light)">Get the Party<br>Started!</div>
    <div class="abs field" style="left:196px;top:1061px;width:80px">Name*</div>
    <div class="abs field" style="left:196px;top:1074px;width:37px">Phone*</div>
    <div class="abs field" style="left:238px;top:1074px;width:38px">Email*</div>
    <div class="abs field" style="left:196px;top:1088px;width:80px">Message*</div>
    <div class="abs btn" style="left:222px;top:1102px;width:28px;height:7px">Send</div>

    <!-- footer -->
    <div class="abs brand" style="left:138px;top:1138px;color:var(--navy)"><span class="mark"></span>KTR</div>
    <div class="abs footer-bar"></div>
    <div class="abs" style="left:22px;top:1163px;font-size:2.6px;color:#c8cde8">© 2018 KTR Events &amp; Visuals</div>
    <div class="abs social" style="left:236px;top:1162px"><i></i><i></i><i></i><i></i><i></i><i></i><i></i></div>
  </section>

  <!-- presentation notes -->
  <aside class="notes">
    <div class="t n-head" style="top:205px">WEBSITE DESIGN FOR &nbsp;<b>KTR EVENTS &amp; VISUALS</b></div>
    <div class="t n-sub" style="top:254px">What’s include to the offer:</div>
    <div class="t n-item" style="top:280px">1. Full Website’s design (8 pages)</div>
    <div class="t n-item" style="top:303px">2. Design Conversion into html</div>
    <div class="t n-item" style="top:326px">3. Convertation into Pagecraft CMS</div>
    <div class="t n-list" style="top:337px;left:58px">* Responsive design<br>* Drag’n Drop builder<br>* Testimonials plugin<br>* Contact form<br>* Social Media integration<br>* Gallery plugin</div>
    <div class="t n-item" style="top:418px">4. Files upload to your hosting</div>
    <div class="t n-item" style="top:441px">5. Full &nbsp;website configuration</div>
    <div class="t n-item" style="top:464px">6. Unlimited design customizations &amp; revisions by your requests</div>
    <div class="t n-item" style="top:487px">7. Fully working website with your content</div>
    <div class="t n-item" style="top:510px">8. After sale support ( lifetime)</div>
    <div class="t n-sub" style="top:550px">Additional Services I offer (paid):</div>
    <div class="t n-list" style="top:576px">Additional pages design,<br>Budget calculation plugin, other special (paid) plugins &amp; components<br>On-page SEO (search engine optimization)<br>Graphic design services<br>Copywriting<br>Website administration &amp; maintenance</div>
    <div class="t n-big" style="top:688px">I hope you will like this design.<br>Looking forward to your feedback.</div>
    <div class="t n-ps" style="top:766px">P.S. Let me know if you will need Live Demo</div>
  </aside>

</div>
</body>
</html>
```